Corporate Power Point Template

Tarnel Holdings, Inc. produces and sells ready-mixed concrete, aggregates, and concrete-related products and services for the construction industry in the United States.

We are looking for a simple and sleek design that will look great on a projector, as well as when printed on paper. We prefer a lighter background color that will not waste ink when printed. We would also like to stay away from wavy banners, or over-the-top graphics that take away from usable space in the deck. Please use a variation of the color scheme in the "Brand Standards" file attached.

Construction

```html
<!DOCTYPE html>
<html lang="en">
<head>
<meta charset="utf-8">
<title>Tarnel Holdings — Corporate Presentation Template</title>
<link href="https://fonts.googleapis.com/css2?family=Roboto:wght@300;400;700&display=swap" rel="stylesheet">
<style>
:root{
  --red:#c8102e;--red-dark:#9e0c24;--ink:#333333;--grey:#6d6e71;--mid:#a7a9ac;
  --light:#ececec;--paper:#ffffff;--band:#58595b;
}
*{box-sizing:border-box}
html,body{margin:0;width:1200px;height:4573px;overflow:hidden;background:var(--paper);font-family:'Roboto',sans-serif;color:var(--ink)}
.deck{display:grid;grid-template-columns:repeat(3,396px);grid-template-rows:repeat(20,1fr);gap:6px;width:1200px;height:4573px}
.slide{position:relative;overflow:hidden;background:var(--paper);box-shadow:inset 0 0 0 1px #dcdcdc}
.slide.dark{background:#4a4a4a}
.slide.greybg{background:#7a7a7a}
.center-col{grid-column:2}
.t{position:absolute;left:12px;top:9px;margin:0;font-size:13px;font-weight:400;text-transform:uppercase;color:var(--ink);letter-spacing:.2px;white-space:nowrap}
.t span{border-bottom:2px solid var(--red)}
.t.w{color:#fff}
.lg{position:absolute;right:10px;top:9px;display:flex;align-items:center;gap:3px;font-size:9px;font-weight:700;color:var(--red);letter-spacing:.5px;white-space:nowrap}
.lg::before{content:"";width:7px;height:7px;background:var(--red)}
.lg.w{color:#fff}.lg.w::before{background:#fff}
.lg.big{font-size:30px;gap:8px}.lg.big::before{width:22px;height:22px}

/* photo placeholders: soft gradients in each scene's main tones */
.ph{position:absolute;background:linear-gradient(160deg,#b4b2ae,#857a70 55%,#4b4846)}
.ph.site{background:linear-gradient(165deg,#c9c7c2,#8d8378 50%,#514c48)}
.ph.crew{background:linear-gradient(150deg,#8a8f96,#6a6258 50%,#3c3a39)}
.ph.flag{background:linear-gradient(135deg,#c23a46,#7d4b57 45%,#34405f)}
.ph.flagred{background:linear-gradient(120deg,#d2424f,#a5585e 50%,#6d7180)}
.ph.sky{background:linear-gradient(170deg,#a9cbe6,#7fa3c2 55%,#56697a)}
.ph.truck{background:linear-gradient(135deg,#cfd3d6,#d9772f 50%,#5d5955)}
.ph.drum{background:linear-gradient(140deg,#e6e6e4,#b5b3ae 45%,#6a6762)}
.ph.dusk{background:linear-gradient(165deg,#8a8785,#5b5856 55%,#2f2e2e)}
.ph.warm{background:linear-gradient(135deg,#d8c4ab,#a2876b 50%,#5f5145)}
.ph.video{background:linear-gradient(150deg,#b84a4f,#8b7c72 50%,#3d4453)}
.ph.face{background:radial-gradient(circle at 50% 40%,#d9c1ae,#9a8a80 70%)}
.map{position:absolute;background:linear-gradient(125deg,#e4c0c5,#c8102e 35%,#9a9a9a 60%,#d7d7d7)}
.map.world{background:linear-gradient(110deg,#e58a96,#cfcfcf 35%,#bdbdbd 60%,#e9e9e9)}

.p{position:absolute;margin:0;font-size:6px;line-height:8px;color:var(--grey)}
.p.w{color:#f1f1f1}
.h{position:absolute;margin:0;font-size:7px;font-weight:700;color:var(--ink);white-space:nowrap}
.h.r{color:var(--red)}.h.w{color:#fff}
.dot{position:absolute;width:14px;height:14px;border-radius:50%;background:var(--red)}
.dot.g{background:var(--grey)}.dot.k{background:#222}.dot.l{background:var(--mid)}
.box{position:absolute}
.red{background:var(--red)}.gry{background:var(--grey)}.blk{background:#262626}.lt{background:var(--light)}.band{background:var(--band)}
.big{position:absolute;margin:0;font-weight:300;color:#fff;text-transform:uppercase}
table.tb{position:absolute;border-collapse:collapse;font-size:6px;color:var(--grey)}
table.tb td,table.tb th{border-bottom:1px solid #ddd;padding:2px 4px;text-align:left}
table.tb th{background:var(--red);color:#fff;font-weight:700}
</style>
</head>
<body>
<main class="deck">

<!-- Row 1 -->
<section class="slide dark">
  <div class="ph site" style="inset:0" role="img" aria-label="Concrete construction site photo"></div>
  <div class="lg big w" style="left:22px;right:auto;top:22px">TARNEL</div>
</section>
<section class="slide dark">
  <div class="ph crew" style="inset:0" role="img" aria-label="Construction workers photo in grey tone"></div>
  <div class="lg big w" style="left:120px;right:auto;top:90px">TARNEL</div>
</section>
<section class="slide dark">
  <div class="ph flag" style="inset:0" role="img" aria-label="Flag over concrete plant photo"></div>
  <div class="lg big w" style="left:20px;right:auto;top:70px">TARNEL</div>
  <p class="big" style="left:22px;top:118px;font-size:15px">Your Title Here</p>
</section>

<!-- Row 2 -->
<section class="slide dark">
  <div class="ph flagred" style="inset:0" role="img" aria-label="Waving flag photo"></div>
  <p class="big" style="left:12px;top:16px;font-size:15px">Your Title Goes Here</p>
  <div class="lg big w" style="left:12px;right:auto;top:150px;font-size:22px">TARNEL</div>
</section>
<section class="slide dark">
  <div class="ph flagred" style="inset:0" role="img" aria-label="Flag and construction crew photo"></div>
  <div class="box" style="left:196px;top:60px;width:200px;height:100px;background:rgba(255,255,255,.92)"></div>
  <div class="lg" style="left:220px;right:auto;top:76px;font-size:20px">TARNEL</div>
  <p class="h" style="left:220px;top:118px;font-size:11px;font-weight:400;color:var(--grey)">YOUR TITLE HERE</p>
</section>
<section class="slide dark">
  <div class="ph crew" style="inset:0" role="img" aria-label="Team of workers on site photo"></div>
  <div class="dot" style="left:300px;top:40px;width:22px;height:22px"></div>
  <p class="p w" style="left:262px;top:72px;width:120px;font-size:7px;line-height:9px">Coming together is a beginning. Keeping together is progress. Working together is success.</p>
</section>

<!-- Row 3 -->
<section class="slide">
  <h2 class="t"><span>Our</span> Agenda</h2><div class="lg">TARNEL</div>
  <div class="dot g" style="left:24px;top:60px"></div><p class="h" style="left:44px;top:60px">Agenda Title</p><p class="p" style="left:44px;top:69px;width:130px">Short note on this agenda item.</p>
  <div class="dot g" style="left:24px;top:100px"></div><p class="h" style="left:44px;top:100px">Agenda Title</p><p class="p" style="left:44px;top:109px;width:130px">Short note on this agenda item.</p>
  <div class="dot g" style="left:24px;top:140px"></div><p class="h" style="left:44px;top:140px">Agenda Title</p><p class="p" style="left:44px;top:149px;width:130px">Short note on this agenda item.</p>
  <div class="dot g" style="left:210px;top:60px"></div><p class="h" style="left:230px;top:60px">Agenda Title</p><p class="p" style="left:230px;top:69px;width:130px">Short note on this agenda item.</p>
  <div class="dot g" style="left:210px;top:100px"></div><p class="h" style="left:230px;top:100px">Agenda Title</p><p class="p" style="left:230px;top:109px;width:130px">Short note on this agenda item.</p>
  <div class="dot g" style="left:210px;top:140px"></div><p class="h" style="left:230px;top:140px">Agenda Title</p><p class="p" style="left:230px;top:149px;width:130px">Short note on this agenda item.</p>
</section>
<section class="slide">
  <div class="ph flag" style="left:0;top:0;width:250px;height:223px" role="img" aria-label="Flag and mixer truck photo"></div>
  <div class="ph truck" style="left:40px;top:120px;width:170px;height:103px" role="img" aria-label="Orange mixer truck photo"></div>
  <div class="box band" style="left:250px;top:0;width:146px;height:223px"></div>
  <p class="h w" style="left:262px;top:50px;font-size:12px;font-weight:400">About Us</p>
  <p class="p w" style="left:262px;top:70px;width:124px">We supply ready-mixed concrete and aggregates to builders across the country.</p>
</section>
<section class="slide">
  <h2 class="t"><span>Our</span> Services</h2><div class="lg">TARNEL</div>
  <div class="ph sky" style="left:14px;top:40px;width:200px;height:120px" role="img" aria-label="City construction photo"></div>
  <p class="h" style="left:14px;top:168px">Your Title Here</p><p class="p" style="left:14px;top:178px;width:200px">Brief description of the service offered here.</p>
  <div class="dot" style="left:236px;top:44px"></div><p class="h r" style="left:256px;top:44px">Service Title</p><p class="p" style="left:256px;top:53px;width:120px">Short service note.</p>
  <div class="dot g" style="left:236px;top:90px"></div><p class="h r" style="left:256px;top:90px">Service Title</p><p class="p" style="left:256px;top:99px;width:120px">Short service note.</p>
  <div class="dot g" style="left:236px;top:136px"></div><p class="h r" style="left:256px;top:136px">Service Title</p><p class="p" style="left:256px;top:145px;width:120px">Short service note.</p>
</section>

<!-- Row 4 -->
<section class="slide">
  <h2 class="t"><span>Quote</span> Area</h2><div class="lg">TARNEL</div>
  <div class="ph drum" style="left:0;top:32px;width:396px;height:115px" role="img" aria-label="Concrete mixer drum close-up photo"></div>
  <div class="box band" style="left:0;top:147px;width:396px;height:76px"></div>
  <p class="p w" style="left:20px;top:165px;width:300px;font-size:7px;line-height:9px">Quality concrete is poured one truck at a time, with care on every job.</p>
</section>
<section class="slide">
  <div class="box lt" style="left:20px;top:22px;width:70px;height:32px"></div><div class="box lt" style="left:163px;top:22px;width:70px;height:32px"></div><div class="box lt" style="left:306px;top:22px;width:70px;height:32px"></div>
  <div class="box lt" style="left:20px;top:96px;width:70px;height:32px"></div><div class="box lt" style="left:306px;top:96px;width:70px;height:32px"></div>
  <div class="box lt" style="left:20px;top:168px;width:70px;height:32px"></div><div class="box lt" style="left:163px;top:168px;width:70px;height:32px"></div><div class="box lt" style="left:306px;top:168px;width:70px;height:32px"></div>
  <div class="box red" style="left:128px;top:82px;width:140px;height:58px"></div>
  <p class="big" style="left:138px;top:94px;font-size:12px;line-height:16px;text-align:center;width:120px">Our Awesome Client</p>
</section>
<section class="slide">
  <h2 class="t"><span>Text</span> Area</h2><div class="lg">TARNEL</div>
  <p class="h" style="left:14px;top:42px">This is a place for your header text. Insert your text here.</p>
  <p class="p" style="left:14px;top:58px;width:368px">Use this area for body copy about the project, its scope, the team, the schedule and the expected results for the client.</p>
  <p class="p" style="left:14px;top:84px;width:368px">A second paragraph can describe supply capacity, plant locations and delivery.</p>
  <p class="p" style="left:14px;top:104px;width:368px">A third paragraph can close with next steps and contact details.</p>
</section>

<!-- Row 5 -->
<section class="slide dark">
  <div class="ph dusk" style="inset:0" role="img" aria-label="Construction site background photo"></div>
  <h2 class="t w"><span>Our</span> Vision &amp; Mission</h2>
  <p class="h w" style="left:16px;top:58px;font-size:9px;font-weight:400">Our Vision</p><p class="p w" style="left:16px;top:72px;width:160px">Build lasting structures with reliable material.</p>
  <p class="h w" style="left:210px;top:58px;font-size:9px;font-weight:400">Our Mission</p><p class="p w" style="left:210px;top:72px;width:160px">Deliver quality concrete on time, every time.</p>
</section>
<section class="slide">
  <h2 class="t"><span>Text</span> Area</h2><div class="lg">TARNEL</div>
  <div class="ph site" style="left:0;top:40px;width:120px;height:183px" role="img" aria-label="Concrete plant photo"></div>
  <p class="h r" style="left:136px;top:50px">This is a place for your header text.</p>
  <p class="p" style="left:136px;top:66px;width:244px">Insert your text here and replace this text with your own copy for the section.</p>
  <p class="p" style="left:136px;top:92px;width:244px">Add more detail about the project, partners and results.</p>
</section>
<section class="slide">
  <h2 class="t"><span>SWOT</span> Analysis</h2><div class="lg">TARNEL</div>
  <div class="box red" style="left:168px;top:62px;width:30px;height:30px"></div><div class="box gry" style="left:200px;top:62px;width:30px;height:30px"></div>
  <div class="box blk" style="left:168px;top:94px;width:30px;height:30px"></div><div class="box red" style="left:200px;top:94px;width:30px;height:30px"></div>
  <p class="h" style="left:240px;top:64px;font-weight:400">• Strengths</p><p class="h" style="left:240px;top:108px;font-weight:400">• Weaknesses</p>
  <p class="h" style="left:116px;top:74px;font-weight:400">• Threats</p><p class="h" style="left:100px;top:120px;font-weight:400">• Opportunities</p>
</section>

<!-- Row 6 -->
<section class="slide">
  <div class="ph site" style="left:0;top:0;width:170px;height:223px" role="img" aria-label="Workers at plant photo"></div>
  <div class="lg w" style="left:20px;right:auto;top:150px;font-size:16px">TARNEL</div>
  <p class="h" style="left:186px;top:34px;font-size:10px;font-weight:400">YOUR TITLE GOES HERE</p>
  <div class="dot" style="left:190px;top:70px;width:10px;height:10px"></div><p class="h r" style="left:206px;top:70px">Your Text Here</p><p class="p" style="left:206px;top:79px;width:170px">Short supporting note.</p>
  <div class="dot g" style="left:190px;top:110px;width:10px;height:10px"></div><p class="h" style="left:206px;top:110px">Your Text Here</p><p class="p" style="left:206px;top:119px;width:170px">Short supporting note.</p>
</section>
<section class="slide">
  <h2 class="t"><span>Your</span> Title Goes Here</h2><div class="lg">TARNEL</div>
  <div class="ph warm" style="left:14px;top:40px;width:60px;height:80px" role="img" aria-label="Site photo"></div>
  <div class="ph sky" style="left:80px;top:40px;width:150px;height:80px" role="img" aria-label="Crane photo"></div>
  <div class="box red" style="left:14px;top:126px;width:80px;height:84px"></div><p class="h w" style="left:20px;top:132px">Heading Goes Here</p>
  <div class="ph crew" style="left:100px;top:126px;width:130px;height:84px" role="img" aria-label="Building photo"></div>
  <div class="ph warm" style="left:236px;top:40px;width:146px;height:170px" role="img" aria-label="Concrete pour photo"></div>
</section>
<section class="slide">
  <div class="ph sky" style="left:0;top:0;width:260px;height:223px" role="img" aria-label="Glass office tower photo"></div>
  <div class="box band" style="left:260px;top:0;width:136px;height:223px"></div>
  <p class="p w" style="left:272px;top:30px;width:112px;font-size:7px;line-height:9px">This is a place for your header text. Insert your text here.</p>
  <div class="dot" style="left:272px;top:90px;width:10px;height:10px"></div><p class="p w" style="left:288px;top:91px;width:96px">Your text here</p>
  <div class="dot" style="left:272px;top:120px;width:10px;height:10px"></div><p class="p w" style="left:288px;top:121px;width:96px">Your text here</p>
  <div class="dot" style="left:272px;top:150px;width:10px;height:10px"></div><p class="p w" style="left:288px;top:151px;width:96px">Your text here</p>
</section>

<!-- Row 7 -->
<section class="slide">
  <div class="box gry" style="left:0;top:0;width:140px;height:90px"></div>
  <div class="lg w" style="left:16px;right:auto;top:34px;font-size:16px">TARNEL</div>
  <div class="ph site" style="left:140px;top:0;width:130px;height:90px" role="img" aria-label="Site aerial photo"></div>
  <div class="ph sky" style="left:0;top:92px;width:135px;height:131px" role="img" aria-label="City skyline photo"></div>
  <div class="ph warm" style="left:137px;top:92px;width:133px;height:131px" role="img" aria-label="Road works photo"></div>
  <p class="h" style="left:282px;top:70px;font-size:10px;font-weight:400;white-space:normal;width:100px;line-height:13px">YOUR TITLE GOES HERE</p>
</section>
<section class="slide">
  <h2 class="t"><span>Your</span> Title Goes Here</h2><div class="lg">TARNEL</div>
  <p class="p" style="left:14px;top:46px;width:150px;font-size:7px;line-height:9px">This is a place for your header text. Insert your text here, just replace this text.</p>
  <div class="ph sky" style="left:180px;top:40px;width:64px;height:170px" role="img" aria-label="Crane photo"></div>
  <div class="ph sky" style="left:248px;top:40px;width:64px;height:170px" role="img" aria-label="Crane photo"></div>
  <div class="ph sky" style="left:316px;top:40px;width:64px;height:170px" role="img" aria-label="Crane photo"></div>
</section>
<section class="slide">
  <h2 class="t"><span>Our</span> Differences</h2><div class="lg">TARNEL</div>
  <div class="dot" style="left:16px;top:48px;width:10px;height:10px"></div><p class="p" style="left:32px;top:49px;width:140px">Our first key difference</p>
  <div class="dot" style="left:16px;top:78px;width:10px;height:10px"></div><p class="p" style="left:32px;top:79px;width:140px">Our second key difference</p>
  <div class="dot" style="left:16px;top:108px;width:10px;height:10px"></div><p class="p" style="left:32px;top:109px;width:140px">Our third key difference</p>
  <div class="dot" style="left:16px;top:138px;width:10px;height:10px"></div><p class="p" style="left:32px;top:139px;width:140px">Our fourth key difference</p>
  <div class="ph truck" style="left:200px;top:40px;width:182px;height:84px" role="img" aria-label="Mixer trucks photo"></div>
  <div class="ph drum" style="left:200px;top:128px;width:182px;height:82px" role="img" aria-label="Concrete pour photo"></div>
</section>

<!-- Row 8 -->
<section class="slide">
  <h2 class="t"><span>Two</span> Column Description</h2><div class="lg">TARNEL</div>
  <p class="h" style="left:14px;top:42px;font-weight:400;white-space:normal;width:360px">This is a place for your header text. Insert your text here, just replace the text with your own text.</p>
  <p class="p" style="left:14px;top:74px;width:176px">Left column body copy describing the topic in a few short lines of text.</p>
  <p class="p" style="left:206px;top:74px;width:176px">Right column body copy describing the topic in a few short lines of text.</p>
</section>
<section class="slide dark">
  <div class="ph dusk" style="inset:0" role="img" aria-label="Dark coffee table photo"></div>
  <div class="lg w">TARNEL</div>
  <div class="dot" style="left:191px;top:84px;background:#fff"></div>
  <p class="big" style="left:0;width:396px;text-align:center;top:104px;font-size:9px">Coffee Break</p>
  <p class="p w" style="left:0;width:396px;text-align:center;top:118px">Back in 15 minutes</p>
</section>
<section class="slide">
  <h2 class="t"><span>Three</span> Column Description</h2><div class="lg">TARNEL</div>
  <p class="h" style="left:14px;top:42px;font-weight:400;white-space:normal;width:360px">This is a place for your header text. Insert your text here, just replace the text with your own text.</p>
  <p class="p" style="left:14px;top:74px;width:114px">First column copy in a few short lines.</p>
  <p class="p" style="left:141px;top:74px;width:114px">Second column copy in a few short lines.</p>
  <p class="p" style="left:268px;top:74px;width:114px">Third column copy in a few short lines.</p>
</section>

<!-- Row 9 -->
<section class="slide">
  <div class="ph drum" style="inset:0" role="img" aria-label="Mixer drum and crane photo"></div>
  <div class="box red" style="left:190px;top:0;width:110px;height:223px;opacity:.9"></div>
  <div class="lg w" style="left:204px;right:auto;top:20px;font-size:14px">TARNEL</div>
  <div class="dot" style="left:206px;top:60px;background:#fff;width:10px;height:10px"></div><div class="dot" style="left:226px;top:60px;background:#fff;width:10px;height:10px"></div><div class="dot" style="left:246px;top:60px;background:#fff;width:10px;height:10px"></div>
  <p class="big" style="left:204px;top:110px;font-size:10px;width:90px">Your Title Goes Here</p>
</section>
<section class="slide">
  <h2 class="t"><span>Your</span> Title Goes Here</h2><div class="lg">TARNEL</div>
  <div class="dot" style="left:16px;top:52px;width:10px;height:10px"></div><p class="h r" style="left:32px;top:53px">Service Name Here</p>
  <div class="dot" style="left:16px;top:82px;width:10px;height:10px"></div><p class="h r" style="left:32px;top:83px">Service Name Here</p>
  <div class="dot" style="left:16px;top:112px;width:10px;height:10px"></div><p class="h r" style="left:32px;top:113px">Service Name Here</p>
  <div class="box red" style="left:196px;top:46px;width:24px;height:24px"></div><p class="big" style="left:203px;top:49px;font-size:14px">1</p><div class="box lt" style="left:220px;top:46px;width:160px;height:24px"></div>
  <div class="box red" style="left:196px;top:78px;width:24px;height:24px"></div><p class="big" style="left:202px;top:81px;font-size:14px">2</p><div class="box lt" style="left:220px;top:78px;width:160px;height:24px"></div>
  <div class="box red" style="left:196px;top:110px;width:24px;height:24px"></div><p class="big" style="left:202px;top:113px;font-size:14px">3</p><div class="box lt" style="left:220px;top:110px;width:160px;height:24px"></div>
</section>
<section class="slide greybg">
  <div class="ph flagred" style="left:0;top:60px;width:210px;height:110px" role="img" aria-label="Red and white flag stripes photo"></div>
  <div class="lg w" style="left:230px;right:auto;top:80px;font-size:18px">TARNEL</div>
  <p class="big" style="left:230px;top:112px;font-size:11px">Divider Title Here</p>
  <p class="p w" style="left:230px;top:128px">Your subtitle goes here</p>
</section>

<!-- Row 10 -->
<section class="slide">
  <h2 class="t"><span>Four</span> Bullets With Paragraph</h2><div class="lg">TARNEL</div>
  <div class="dot" style="left:16px;top:48px"></div><p class="h r" style="left:36px;top:50px">Your Title</p>
  <div class="dot g" style="left:96px;top:48px"></div><p class="h" style="left:116px;top:50px">Your Title</p>
  <div class="dot g" style="left:16px;top:100px"></div><p class="h" style="left:36px;top:102px">Your Title</p>
  <div class="dot g" style="left:96px;top:100px"></div><p class="h" style="left:116px;top:102px">Your Title</p>
  <p class="h" style="left:200px;top:50px;font-weight:400">Heading Goes Here</p>
  <p class="p" style="left:200px;top:64px;width:180px">Paragraph copy for this slide sits here in a few short lines of text.</p>
</section>
<section class="slide">
  <h2 class="t"><span>Your</span> Title</h2><div class="lg">TARNEL</div>
  <p class="h" style="left:14px;top:46px;font-weight:400">Heading Goes Here</p>
  <p class="p" style="left:14px;top:60px;width:110px">Short body copy for this topic goes here.</p>
  <div class="ph sky" style="left:140px;top:40px;width:110px;height:170px" role="img" aria-label="Control tower photo"></div>
  <div class="ph truck" style="left:256px;top:40px;width:126px;height:170px" role="img" aria-label="Mixer truck photo"></div>
</section>
<section class="slide">
  <h2 class="t"><span>Text</span> &amp; Bullet Area</h2><div class="lg">TARNEL</div>
  <p class="h" style="left:14px;top:46px;font-weight:400">Heading Goes Here</p>
  <p class="p" style="left:14px;top:60px;width:170px">Body copy for this section goes here in a few short lines.</p>
  <div class="dot" style="left:210px;top:48px;width:10px;height:10px"></div><p class="h r" style="left:226px;top:49px">Your Text Here</p>
  <div class="dot" style="left:210px;top:80px;width:10px;height:10px"></div><p class="h r" style="left:226px;top:81px">Your Text Here</p>
  <div class="dot" style="left:210px;top:112px;width:10px;height:10px"></div><p class="h r" style="left:226px;top:113px">Your Text Here</p>
  <div class="dot" style="left:210px;top:144px;width:10px;height:10px"></div><p class="h r" style="left:226px;top:145px">Your Text Here</p>
</section>

<!-- Row 11 -->
<section class="slide">
  <h2 class="t"><span>Paragraph</span> With Three Bullet</h2><div class="lg">TARNEL</div>
  <p class="h" style="left:14px;top:42px;font-weight:400">This is a place for your header text. Insert your text here.</p>
  <div class="dot" style="left:20px;top:90px"></div><p class="p" style="left:14px;top:110px;width:110px">First bullet copy here.</p>
  <div class="dot" style="left:147px;top:90px"></div><p class="p" style="left:141px;top:110px;width:110px">Second bullet copy here.</p>
  <div class="dot" style="left:274px;top:90px"></div><p class="p" style="left:268px;top:110px;width:110px">Third bullet copy here.</p>
</section>
<section class="slide">
  <h2 class="t"><span>Multiple</span> Column Area</h2><div class="lg">TARNEL</div>
  <div class="dot" style="left:40px;top:54px"></div><div class="dot" style="left:132px;top:54px"></div><div class="dot" style="left:224px;top:54px"></div><div class="dot" style="left:316px;top:54px"></div>
  <p class="h" style="left:16px;top:90px;font-weight:400">Heading Goes Here</p><p class="p" style="left:16px;top:102px;width:170px">Column copy in a few short lines.</p>
  <p class="h" style="left:206px;top:90px;font-weight:400">Heading Goes Here</p><p class="p" style="left:206px;top:102px;width:170px">Column copy in a few short lines.</p>
</section>
<section class="slide">
  <h2 class="t"><span>Monthly</span> Subscription</h2><div class="lg">TARNEL</div>
  <div class="box gry" style="left:0;top:62px;width:396px;height:40px"></div>
  <div class="box blk" style="left:70px;top:52px;width:76px;height:56px"></div><p class="big" style="left:88px;top:62px;font-size:14px">$300</p>
  <div class="box red" style="left:160px;top:46px;width:76px;height:64px"></div><p class="big" style="left:178px;top:60px;font-size:14px">$600</p>
  <div class="box blk" style="left:250px;top:52px;width:76px;height:56px"></div><p class="big" style="left:268px;top:62px;font-size:14px">$400</p>
  <p class="p" style="left:70px;top:118px;width:76px">Basic plan list</p><p class="p" style="left:160px;top:118px;width:76px">Premium plan list</p><p class="p" style="left:250px;top:118px;width:76px">Standard plan list</p>
</section>

<!-- Row 12 -->
<section class="slide">
  <p class="h" style="left:14px;top:14px;font-size:10px;font-weight:400;white-space:normal;width:90px;line-height:13px">VIDEO TITLE GOES HERE</p>
  <div class="box blk" style="left:120px;top:30px;width:220px;height:134px;border-radius:4px"></div>
  <div class="ph video" style="left:126px;top:36px;width:208px;height:118px" role="img" aria-label="Video frame of plant and crew"></div>
  <svg class="box" style="left:216px;top:82px" width="26" height="22" viewBox="0 0 26 22"><rect width="26" height="22" rx="5" fill="#c8102e"/><path d="M10 6l8 5-8 5z" fill="#fff"/></svg>
  <div class="box lt" style="left:200px;top:164px;width:60px;height:20px"></div><div class="box lt" style="left:180px;top:184px;width:100px;height:4px"></div>
</section>
<section class="slide">
  <h2 class="t"><span>Four</span> Column Area</h2><div class="lg">TARNEL</div>
  <div class="box red" style="left:16px;top:50px;width:84px;height:84px"></div><div class="box gry" style="left:108px;top:50px;width:84px;height:84px"></div>
  <div class="box blk" style="left:200px;top:50px;width:84px;height:84px"></div><div class="box band" style="left:292px;top:50px;width:84px;height:84px"></div>
  <p class="h w" style="left:30px;top:110px">Your Text Here</p><p class="h w" style="left:122px;top:110px">Your Text Here</p><p class="h w" style="left:214px;top:110px">Your Text Here</p><p class="h w" style="left:306px;top:110px">Your Text Here</p>
  <p class="p" style="left:16px;top:144px;width:84px">Column note.</p><p class="p" style="left:108px;top:144px;width:84px">Column note.</p><p class="p" style="left:200px;top:144px;width:84px">Column note.</p><p class="p" style="left:292px;top:144px;width:84px">Column note.</p>
</section>
<section class="slide">
  <h2 class="t"><span>Four</span> Column Area</h2><div class="lg">TARNEL</div>
  <div class="dot" style="left:40px;top:50px;width:28px;height:28px"></div><div class="dot k" style="left:134px;top:50px;width:28px;height:28px"></div><div class="dot" style="left:228px;top:50px;width:28px;height:28px"></div><div class="dot k" style="left:322px;top:50px;width:28px;height:28px"></div>
  <p class="h" style="left:36px;top:90px">Your Title</p><p class="h" style="left:130px;top:90px">Your Title</p><p class="h" style="left:224px;top:90px">Your Title</p><p class="h" style="left:318px;top:90px">Your Title</p>
  <p class="p" style="left:20px;top:102px;width:70px;text-align:center">Column note.</p><p class="p" style="left:114px;top:102px;width:70px;text-align:center">Column note.</p><p class="p" style="left:208px;top:102px;width:70px;text-align:center">Column note.</p><p class="p" style="left:302px;top:102px;width:70px;text-align:center">Column note.</p>
</section>

<!-- Row 13 -->
<section class="slide">
  <h2 class="t"><span>Our</span> Services</h2><div class="lg">TARNEL</div>
  <div class="dot" style="left:16px;top:50px"></div><p class="h" style="left:34px;top:53px">Service</p>
  <div class="dot k" style="left:110px;top:50px"></div><p class="h" style="left:128px;top:53px">Service</p>
  <div class="dot" style="left:204px;top:50px"></div><p class="h" style="left:222px;top:53px">Service</p>
  <div class="dot k" style="left:298px;top:50px"></div><p class="h" style="left:316px;top:53px">Service</p>
  <div class="dot k" style="left:16px;top:100px"></div><p class="h" style="left:34px;top:103px">Service</p>
  <div class="dot" style="left:110px;top:100px"></div><p class="h" style="left:128px;top:103px">Service</p>
  <div class="dot k" style="left:204px;top:100px"></div><p class="h" style="left:222px;top:103px">Service</p>
  <div class="dot" style="left:298px;top:100px"></div><p class="h" style="left:316px;top:103px">Service</p>
</section>
<section class="slide dark" style="background:#3a3a3a">
  <div class="ph flagred" style="left:0;top:80px;width:210px;height:110px" role="img" aria-label="Red and white flag stripes photo"></div>
  <div class="lg w" style="left:230px;right:auto;top:80px;font-size:18px">TARNEL</div>
  <p class="big" style="left:230px;top:112px;font-size:11px">Divider Title Here</p>
  <p class="p w" style="left:230px;top:128px">Your subtitle goes here</p>
</section>
<section class="slide">
  <h2 class="t"><span>Key</span> Points Area</h2><div class="lg">TARNEL</div>
  <div class="box lt" style="left:0;top:56px;width:396px;height:40px"></div>
  <div class="dot" style="left:50px;top:46px;width:60px;height:60px"></div><div class="dot g" style="left:130px;top:46px;width:60px;height:60px"></div>
  <div class="dot l" style="left:210px;top:46px;width:60px;height:60px"></div><div class="dot" style="left:290px;top:46px;width:60px;height:60px"></div>
  <p class="p" style="left:50px;top:118px;width:60px;text-align:center">Key point</p><p class="p" style="left:130px;top:118px;width:60px;text-align:center">Key point</p><p class="p" style="left:210px;top:118px;width:60px;text-align:center">Key point</p><p class="p" style="left:290px;top:118px;width:60px;text-align:center">Key point</p>
</section>

<!-- Row 14 -->
<section class="slide">
  <h2 class="t"><span>Workflow</span> Area</h2><div class="lg">TARNEL</div>
  <svg class="box" style="left:16px;top:60px" width="364" height="70" viewBox="0 0 364 70">
    <path d="M10 60a40 40 0 0 1 80 0" stroke="#6d6e71" stroke-width="14" fill="none"/>
    <path d="M100 20a40 40 0 0 0 80 0" stroke="#c8102e" stroke-width="14" fill="none"/>
    <path d="M190 60a40 40 0 0 1 80 0" stroke="#6d6e71" stroke-width="14" fill="none"/>
    <path d="M280 20a40 40 0 0 0 80 0" stroke="#c8102e" stroke-width="14" fill="none"/>
  </svg>
  <p class="h r" style="left:40px;top:140px">Step 1</p><p class="h r" style="left:130px;top:140px">Step 2</p><p class="h r" style="left:220px;top:140px">Step 3</p><p class="h r" style="left:310px;top:140px">Step 4</p>
</section>
<section class="slide">
  <h2 class="t"><span>Timeline</span></h2><div class="lg">TARNEL</div>
  <div class="box lt" style="left:20px;top:104px;width:356px;height:2px"></div>
  <div class="dot g" style="left:50px;top:90px;width:30px;height:30px"></div><div class="dot" style="left:110px;top:70px;width:30px;height:30px"></div>
  <div class="dot k" style="left:170px;top:90px;width:30px;height:30px"></div><div class="dot g" style="left:230px;top:110px;width:30px;height:30px"></div><div class="dot" style="left:290px;top:90px;width:30px;height:30px"></div>
  <p class="p" style="left:57px;top:126px">2014</p><p class="p" style="left:117px;top:58px">2015</p><p class="p" style="left:177px;top:126px">2016</p><p class="p" style="left:237px;top:146px">2017</p><p class="p" style="left:297px;top:126px">2018</p>
</section>
<section class="slide">
  <h2 class="t"><span>This</span> Is Line Chart Slide</h2><div class="lg">TARNEL</div>
  <svg class="box" style="left:190px;top:44px" width="190" height="100" viewBox="0 0 190 100">
    <g stroke="#e2e2e2"><line x1="0" y1="20" x2="190" y2="20"/><line x1="0" y1="50" x2="190" y2="50"/><line x1="0" y1="80" x2="190" y2="80"/></g>
    <polyline points="0,80 50,30 100,70 150,20 190,50" fill="none" stroke="#c8102e" stroke-width="2"/>
    <polyline points="0,40 50,60 100,30 150,70 190,40" fill="none" stroke="#6d6e71" stroke-width="2"/>
  </svg>
  <p class="p" style="left:16px;top:50px;width:160px">Describe the trend shown in the chart here.</p>
</section>

<!-- Row 15 -->
<section class="slide">
  <h2 class="t"><span>Market</span> Performance</h2><div class="lg">TARNEL</div>
  <svg class="box" style="left:16px;top:50px" width="364" height="100" viewBox="0 0 364 100">
    <g fill="#c8102e"><rect x="0" y="40" width="12" height="60"/><rect x="36" y="20" width="12" height="80"/><rect x="72" y="50" width="12" height="50"/><rect x="108" y="10" width="12" height="90"/><rect x="196" y="30" width="12" height="70"/><rect x="232" y="50" width="12" height="50"/><rect x="268" y="20" width="12" height="80"/><rect x="304" y="40" width="12" height="60"/></g>
    <g fill="#333"><rect x="14" y="60" width="12" height="40"/><rect x="50" y="40" width="12" height="60"/><rect x="86" y="30" width="12" height="70"/><rect x="122" y="50" width="12" height="50"/><rect x="210" y="50" width="12" height="50"/><rect x="246" y="20" width="12" height="80"/><rect x="282" y="60" width="12" height="40"/><rect x="318" y="10" width="12" height="90"/></g>
  </svg>
  <p class="p" style="left:16px;top:160px">Q1 to Q4 sales</p><p class="p" style="left:212px;top:160px">Q1 to Q4 volume</p>
</section>
<section class="slide">
  <h2 class="t"><span>Our</span> Team</h2><div class="lg">TARNEL</div>
  <div class="dot ph face" style="left:24px;top:46px;width:30px;height:30px" role="img" aria-label="Team member portrait"></div><p class="h" style="left:62px;top:50px">Team Name</p><p class="p" style="left:62px;top:60px">Role title</p>
  <div class="dot ph face" style="left:210px;top:46px;width:30px;height:30px" role="img" aria-label="Team member portrait"></div><p class="h" style="left:248px;top:50px">Team Name</p><p class="p" style="left:248px;top:60px">Role title</p>
  <div class="dot ph face" style="left:24px;top:110px;width:30px;height:30px" role="img" aria-label="Team member portrait"></div><p class="h" style="left:62px;top:114px">Team Name</p><p class="p" style="left:62px;top:124px">Role title</p>
  <div class="dot ph face" style="left:210px;top:110px;width:30px;height:30px" role="img" aria-label="Team member portrait"></div><p class="h" style="left:248px;top:114px">Team Name</p><p class="p" style="left:248px;top:124px">Role title</p>
</section>
<section class="slide">
  <h2 class="t"><span>Your</span> Blank Slide</h2><div class="lg">TARNEL</div>
  <div class="box" style="left:40px;top:70px;width:320px;height:14px;background:#f6e0e3"></div>
  <div class="box" style="left:40px;top:100px;width:320px;height:14px;background:#f6e0e3"></div>
  <div class="box" style="left:40px;top:130px;width:320px;height:14px;background:#f6e0e3"></div>
</section>

<!-- Row 16 -->
<section class="slide">
  <h2 class="t"><span>Customer</span> Testimonials</h2><div class="lg">TARNEL</div>
  <div class="dot ph face" style="left:168px;top:34px;width:60px;height:60px" role="img" aria-label="Customer portrait"></div>
  <p class="p" style="left:100px;top:100px;width:200px;text-align:center">Reliable supply and friendly crews on every pour.</p>
  <div class="box band" style="left:0;top:130px;width:396px;height:93px"></div>
  <div class="dot" style="left:60px;top:146px;background:#fff"></div><div class="dot" style="left:190px;top:146px;background:#fff"></div><div class="dot" style="left:320px;top:146px;background:#fff"></div>
  <p class="p w" style="left:27px;top:170px;width:80px;text-align:center">Client note.</p><p class="p w" style="left:157px;top:170px;width:80px;text-align:center">Client note.</p><p class="p w" style="left:287px;top:170px;width:80px;text-align:center">Client note.</p>
</section>
<section class="slide">
  <h2 class="t"><span>Financial</span> Report</h2><div class="lg">TARNEL</div>
  <svg class="box" style="left:20px;top:44px" width="120" height="120" viewBox="-60 -60 120 120">
    <circle r="50" fill="#6d6e71"/><path d="M0 0 L0 -50 A50 50 0 1 1 -12.5 48.4 Z" fill="#c8102e"/><path d="M0 0 L-12.5 48.4 A50 50 0 0 1 -48 -14 Z" fill="#333"/>
  </svg>
  <p class="h r" style="left:20px;top:176px;font-size:14px;font-weight:400">54%</p>
  <div class="dot" style="left:200px;top:50px;width:10px;height:10px"></div><p class="p" style="left:216px;top:51px">Your text here</p>
  <div class="dot g" style="left:200px;top:80px;width:10px;height:10px"></div><p class="p" style="left:216px;top:81px">Your text here</p>
  <div class="dot k" style="left:200px;top:110px;width:10px;height:10px"></div><p class="p" style="left:216px;top:111px">Your text here</p>
</section>
<section class="slide">
  <h2 class="t"><span>Bullet</span> &amp; Chart Area</h2><div class="lg">TARNEL</div>
  <div class="box red" style="left:16px;top:50px;width:150px;height:10px"></div><div class="box gry" style="left:16px;top:64px;width:110px;height:10px"></div>
  <div class="box red" style="left:16px;top:90px;width:120px;height:10px"></div><div class="box gry" style="left:16px;top:104px;width:160px;height:10px"></div>
  <div class="box red" style="left:16px;top:130px;width:90px;height:10px"></div><div class="box gry" style="left:16px;top:144px;width:140px;height:10px"></div>
  <p class="p" style="left:220px;top:50px">• Your text here</p><p class="p" style="left:220px;top:80px">• Your text here</p><p class="p" style="left:220px;top:110px">• Your text here</p><p class="p" style="left:220px;top:140px">• Your text here</p>
</section>

<!-- Row 17 -->
<section class="slide">
  <h2 class="t"><span>Triangle</span> Infographic</h2><div class="lg">TARNEL</div>
  <svg class="box" style="left:30px;top:40px" width="120" height="140" viewBox="0 0 120 140">
    <path d="M60 0 L80 35 L40 35 Z" fill="#333"/><path d="M38 39 L82 39 L100 72 L20 72 Z" fill="#c8102e"/>
    <path d="M18 76 L102 76 L118 106 L2 106 Z" fill="#6d6e71"/><path d="M0 110 L120 110 L120 120 L0 120 Z" fill="#a7a9ac"/>
  </svg>
  <p class="h" style="left:170px;top:56px">Content Title</p><p class="h" style="left:190px;top:88px">Content Title</p><p class="h" style="left:210px;top:120px">Content Title</p><p class="h" style="left:230px;top:152px">Content Title</p>
</section>
<section class="slide">
  <h2 class="t"><span>Digital</span> System</h2><div class="lg">TARNEL</div>
  <svg class="box" style="left:148px;top:50px" width="100" height="100" viewBox="-50 -50 100 100">
    <circle r="36" fill="none" stroke="#6d6e71" stroke-width="18"/>
    <circle r="36" fill="none" stroke="#c8102e" stroke-width="18" stroke-dasharray="130 96" transform="rotate(-90)"/>
  </svg>
  <p class="p" style="left:40px;top:70px">Your text here</p><p class="p" style="left:40px;top:120px">Your text here</p>
  <p class="p" style="left:290px;top:70px">Your text here</p><p class="p" style="left:290px;top:120px">Your text here</p>
</section>
<section class="slide">
  <h2 class="t"><span>Advanced</span></h2><div class="lg">TARNEL</div>
  <svg class="box" style="left:150px;top:50px" width="100" height="100" viewBox="0 0 100 100">
    <path d="M48 48 H0 A48 48 0 0 1 48 0 Z" fill="#c8102e"/><path d="M52 48 V0 A48 48 0 0 1 100 48 Z" fill="#333"/>
    <path d="M52 52 H100 A48 48 0 0 1 52 100 Z" fill="#6d6e71"/><path d="M48 52 V100 A48 48 0 0 1 0 52 Z" fill="#a7a9ac"/>
  </svg>
  <p class="p" style="left:40px;top:70px">Your text here</p><p class="p" style="left:40px;top:120px">Your text here</p>
  <p class="p" style="left:290px;top:70px">Your text here</p><p class="p" style="left:290px;top:120px">Your text here</p>
</section>

<!-- Row 18 -->
<section class="slide">
  <h2 class="t"><span>Your</span> Table Here</h2><div class="lg">TARNEL</div>
  <table class="tb" style="left:16px;top:44px;width:364px">
    <tr><th>Item</th><th>2015</th><th>2016</th><th>2017</th><th>2018</th></tr>
    <tr><td>Concrete</td><td>120</td><td>140</td><td>160</td><td>180</td></tr>
    <tr><td>Aggregates</td><td>80</td><td>90</td><td>95</td><td>110</td></tr>
    <tr><td>Precast</td><td>40</td><td>45</td><td>52</td><td>60</td></tr>
    <tr><td>Services</td><td>30</td><td>34</td><td>38</td><td>41</td></tr>
    <tr><td>Total</td><td>270</td><td>309</td><td>345</td><td>391</td></tr>
  </table>
</section>
<section class="slide">
  <h2 class="t"><span>Our</span> Team</h2><div class="lg">TARNEL</div>
  <div class="dot ph face" style="left:158px;top:40px;width:80px;height:80px" role="img" aria-label="Team leader portrait"></div>
  <p class="h" style="left:0;width:396px;text-align:center;top:130px;font-size:9px">Jordan Velk</p>
  <p class="p" style="left:0;width:396px;text-align:center;top:142px">Chief Executive Officer</p>
  <p class="p" style="left:98px;width:200px;text-align:center;top:156px">Leads our plants and delivery teams.</p>
</section>
<section class="slide">
  <h2 class="t"><span>USA</span> Map</h2><div class="lg">TARNEL</div>
  <div class="map" style="left:150px;top:46px;width:232px;height:140px;border-radius:6px" role="img" aria-label="Map of United States with highlighted states in red and grey"></div>
  <div class="dot" style="left:16px;top:60px;width:10px;height:10px"></div><p class="p" style="left:32px;top:61px">Region name</p>
  <div class="dot g" style="left:16px;top:90px;width:10px;height:10px"></div><p class="p" style="left:32px;top:91px">Region name</p>
  <div class="dot k" style="left:16px;top:120px;width:10px;height:10px"></div><p class="p" style="left:32px;top:121px">Region name</p>
</section>

<!-- Row 19 -->
<section class="slide">
  <h2 class="t"><span>Global</span> Experience</h2><div class="lg">TARNEL</div>
  <div class="map world" style="left:16px;top:46px;width:364px;height:150px;border-radius:6px" role="img" aria-label="World map with North America highlighted in red"></div>
  <p class="h r" style="left:40px;top:70px">North America</p><p class="h" style="left:110px;top:96px;font-weight:400">South America</p><p class="h" style="left:200px;top:86px;font-weight:400">Europe</p><p class="h" style="left:290px;top:110px;font-weight:400">Asia</p>
</section>
<section class="slide">
  <h2 class="t"><span>Table</span> Area</h2><div class="lg">TARNEL</div>
  <table class="tb" style="left:36px;top:50px;width:324px">
    <tr><th>Description</th><th>Category 1</th><th>Category 2</th></tr>
    <tr><td>Item one</td><td>12</td><td>18</td></tr>
    <tr><td>Item two</td><td>24</td><td>20</td></tr>
    <tr><td>Item three</td><td>30</td><td>27</td></tr>
    <tr><td>Item four</td><td>16</td><td>22</td></tr>
  </table>
</section>
<section class="slide">
  <h2 class="t"><span>Bullet</span> &amp; Chart Area</h2><div class="lg">TARNEL</div>
  <div class="dot" style="left:16px;top:56px;width:10px;height:10px"></div><p class="p" style="left:32px;top:57px">Your text here</p>
  <div class="dot" style="left:16px;top:86px;width:10px;height:10px"></div><p class="p" style="left:32px;top:87px">Your text here</p>
  <div class="dot" style="left:16px;top:116px;width:10px;height:10px"></div><p class="p" style="left:32px;top:117px">Your text here</p>
  <svg class="box" style="left:240px;top:50px" width="110" height="110" viewBox="-55 -55 110 110">
    <circle r="40" fill="none" stroke="#ececec" stroke-width="16"/>
    <circle r="40" fill="none" stroke="#c8102e" stroke-width="16" stroke-dasharray="150 101" transform="rotate(-90)"/>
  </svg>
  <p class="h r" style="left:210px;top:56px">50%</p><p class="h" style="left:210px;top:150px">30%</p><p class="h" style="left:354px;top:106px">20%</p>
</section>

<!-- Row 20 -->
<section class="slide dark center-col">
  <div class="ph crew" style="left:0;top:0;width:200px;height:223px" role="img" aria-label="Construction crew photo"></div>
  <p class="big" style="left:16px;top:20px;font-size:12px">Thank You</p>
  <div class="box" style="left:200px;top:0;width:196px;height:223px;background:#2e2e2e"></div>
  <div class="lg w" style="left:216px;right:auto;top:30px;font-size:18px">TARNEL</div>
  <p class="big" style="left:216px;top:66px;font-size:9px">Our Contact</p>
  <p class="p w" style="left:216px;top:84px">120 Harbor Road, Suite 4</p>
  <p class="p w" style="left:216px;top:98px">(555) 010-2468</p>
  <p class="p w" style="left:216px;top:112px">hello@tarnelholdings.example</p>
  <p class="p w" style="left:216px;top:126px">www.tarnelholdings.example</p>
  <div class="box red" style="left:200px;top:200px;width:196px;height:23px"></div>
</section>

</main>
</body>
</html>
```